Talents and colours poster for home office

The objective is to illustrate/communicate and remember 5 talents and 4 colours of the personality.

The infographic will be hanged on the wall of an home office. It need to be simple and clear. Illustrations and pictograms can be used. It can be artistic.

Here's the content:

5 talents,scaling in priority from #1 to #5
Ideation / creativity
Winning other over / charisma
Adaptability
Positivity
Empathy

In the files there is a description of what those mean.

You have to include 4 colours, scaling in priority from #1 to #4
Yellow
Green
Red
Blue

I made a sketch just for fun... and to show why I need professionnal skills :)

THX

Industry/Entity Type

Office

Requirements
Should not have
• offensive materials

```html
<!DOCTYPE html>
<html lang="en">
<head>
<meta charset="utf-8">
<title>Talents &amp; Personality</title>
<link rel="stylesheet" href="https://fonts.googleapis.com/css2?family=Oswald:wght@300;400;500&display=swap">
<style>
  :root {
    --sky-light: #f4f4f4;
    --sky-mid: #d9d9d9;
    --sky-dark: #a9a9a9;
    --ring: #f2f2f2;
    --red: #f20000;
    --red-deep: #d80000;
    --green: #0d8f14;
    --green-deep: #013d05;
    --orange: #f46200;
    --orange-deep: #e85700;
    --teal: #00b89a;
    --teal-deep: #00a88b;
    --bubble: #a8388f;
    --white: #ffffff;
    --frame: rgba(255,255,255,0.55);
  }
  * { margin: 0; padding: 0; box-sizing: border-box; }
  html, body { width: 846px; height: 1200px; overflow: hidden; }
  body {
    font-family: "Oswald", "Arial Narrow", sans-serif;
    background: var(--sky-mid);
  }
  .poster {
    position: relative;
    width: 846px;
    height: 1200px;
    overflow: hidden;
    background:
      radial-gradient(ellipse 60% 45% at 50% 30%, var(--sky-light) 0%, rgba(244,244,244,0) 70%),
      radial-gradient(ellipse 70% 40% at 70% 85%, rgba(255,255,255,0.7) 0%, rgba(255,255,255,0) 70%),
      linear-gradient(180deg, var(--sky-dark) 0%, var(--sky-mid) 35%, #e4e4e4 60%, var(--sky-dark) 100%);
  }
  .sky {
    position: absolute; inset: 0;
  }
  .mascot {
    position: absolute;
    left: 300px; top: 8px;
    width: 232px; height: 388px;
    border-radius: 110px 110px 30px 30px;
    background: linear-gradient(180deg, #d9a54a 0%, #f1c9a5 30%, #a8a8a8 55%, #7d7d7d 100%);
  }
  .bubble {
    position: absolute;
    left: 488px; top: 140px;
    width: 316px; height: 224px;
  }
  .bubble svg { position: absolute; inset: 0; }
  .bubble-text {
    position: absolute;
    left: 50px; top: 24px;
    color: var(--white);
    line-height: 1;
  }
  .bubble-title {
    display: block;
    font-weight: 300;
    font-size: 64px;
    letter-spacing: -1px;
    transform: scaleX(0.82);
    transform-origin: left;
  }
  .bubble-sub {
    display: block;
    font-weight: 400;
    font-size: 42px;
    margin-top: -4px;
    transform: scaleX(0.9);
    transform-origin: left;
  }
  .talents { position: absolute; inset: 0; }
  .talent-label {
    position: absolute;
    color: var(--white);
    font-weight: 500;
    font-size: 39px;
    line-height: 1.06;
    padding: 6px 14px;
    border: 1px solid var(--frame);
    letter-spacing: 0.5px;
  }
  .label-ideation { left: 316px; top: 500px; width: 218px; }
  .label-charisma { left: 82px; top: 712px; width: 252px; }
  .label-adaptability { left: 530px; top: 722px; width: 248px; }
  .label-empathy { left: 316px; top: 968px; width: 218px; letter-spacing: 4px; padding: 4px 14px; }
</style>
</head>
<body>
<main class="poster">
  <svg class="sky" width="846" height="1200" viewBox="0 0 846 1200" role="img" aria-label="Cloudy sky with light rays radiating from behind the character">
    <defs>
      <radialGradient id="cloud-glow" cx="50%" cy="50%" r="50%">
        <stop offset="0" stop-color="#ffffff" stop-opacity="0.8"/>
        <stop offset="1" stop-color="#ffffff" stop-opacity="0"/>
      </radialGradient>
    </defs>
    <ellipse cx="120" cy="500" rx="180" ry="90" fill="url(#cloud-glow)"/>
    <ellipse cx="760" cy="520" rx="160" ry="80" fill="url(#cloud-glow)"/>
    <ellipse cx="400" cy="280" rx="260" ry="120" fill="url(#cloud-glow)"/>
  </svg>

  <div class="mascot" role="img" aria-label="Cartoon character giving a thumbs up and pointing down, standing on top of the circles"></div>

  <div class="bubble">
    <svg width="316" height="224" viewBox="0 0 316 224" aria-hidden="true">
      <path d="M40 0 H276 Q316 0 316 40 V200 L312 220 Q270 190 250 176 H40 Q0 176 0 136 V40 Q0 0 40 0 Z" fill="var(--bubble)"/>
    </svg>
    <p class="bubble-text">
      <span class="bubble-title">TALENTS &amp;</span>
      <span class="bubble-sub">personality</span>
    </p>
  </div>

  <svg class="talents" width="846" height="1200" viewBox="0 0 846 1200" aria-hidden="true">
    <defs>
      <radialGradient id="fill-green" cx="70%" cy="40%" r="75%">
        <stop offset="0" stop-color="var(--green)"/>
        <stop offset="0.55" stop-color="#0a7a10"/>
        <stop offset="1" stop-color="var(--green-deep)"/>
      </radialGradient>
      <radialGradient id="fill-red" cx="50%" cy="40%" r="70%">
        <stop offset="0" stop-color="var(--red)"/>
        <stop offset="1" stop-color="var(--red-deep)"/>
      </radialGradient>
      <radialGradient id="fill-orange" cx="50%" cy="40%" r="70%">
        <stop offset="0" stop-color="var(--orange)"/>
        <stop offset="1" stop-color="var(--orange-deep)"/>
      </radialGradient>
      <radialGradient id="fill-teal" cx="50%" cy="40%" r="70%">
        <stop offset="0" stop-color="var(--teal)"/>
        <stop offset="1" stop-color="var(--teal-deep)"/>
      </radialGradient>
      <filter id="soft-shadow" x="-20%" y="-20%" width="140%" height="140%">
        <feDropShadow dx="0" dy="4" stdDeviation="6" flood-color="#000" flood-opacity="0.3"/>
      </filter>
    </defs>
    <g class="circle-empathy" filter="url(#soft-shadow)">
      <circle cx="414" cy="962" r="192" fill="var(--ring)"/>
      <circle cx="414" cy="962" r="183" fill="url(#fill-teal)"/>
    </g>
    <g class="circle-charisma" filter="url(#soft-shadow)">
      <circle cx="226" cy="762" r="192" fill="var(--ring)"/>
      <circle cx="226" cy="762" r="183" fill="url(#fill-green)"/>
    </g>
    <g class="circle-ideation" filter="url(#soft-shadow)">
      <circle cx="414" cy="583" r="192" fill="var(--ring)"/>
      <circle cx="414" cy="583" r="183" fill="url(#fill-red)"/>
    </g>
    <g class="circle-adaptability" filter="url(#soft-shadow)">
      <circle cx="610" cy="762" r="192" fill="var(--ring)"/>
      <circle cx="610" cy="762" r="183" fill="url(#fill-orange)"/>
    </g>
  </svg>

  <p class="talent-label label-ideation">IDEATION /<br>CREATIVITY</p>
  <p class="talent-label label-charisma">WINNING<br>OTHER OVER /<br>CHARISMA</p>
  <p class="talent-label label-adaptability">ADAPTABILITY<br>/ POSITIVITY</p>
  <p class="talent-label label-empathy">EMPATHY</p>
</main>
</body>
</html>
```